Redesign our Product Box!

We have a product box for our pet supplement we are looking to redesign. Please use the photoshop file of the current design for the logo/info/dieline and the concept picture of a bag we would like to see included in the box design.

Ideally the background will be the green with white text, but we really want it to be fun and appealing to pet owners so do not be scared to show your vision.

```html
<!DOCTYPE html>
<html lang="en">
<head>
<meta charset="utf-8">
<title>Marivita Box Dieline</title>
<link rel="stylesheet" href="https://fonts.googleapis.com/css2?family=Source+Sans+3:wght@300;400;600;700;900&family=Roboto+Condensed:wght@300;400;700&display=swap">
<style>
  :root {
    --green: #00a84f;
    --white: #ffffff;
    --ink: #404040;
    --dark: #1f1f1f;
    --cut: #d62a2a;
    --fold: #2e4b9b;
    --rule: #8cc63f;
    --paper: #ffffff;
    --photo-light: #f3e6d2;
    --photo-mid: #d9a868;
    --photo-dark: #b07a3c;
  }
  * { margin: 0; padding: 0; box-sizing: border-box; }
  html, body { width: 1097px; height: 1200px; overflow: hidden; background: var(--paper); }
  .canvas { position: relative; width: 1097px; height: 1200px; font-family: "Source Sans 3", sans-serif; color: var(--ink); }
  .dieline { position: absolute; inset: 0; }
  .txt { position: absolute; text-align: center; }
  .cond { font-family: "Roboto Condensed", sans-serif; font-weight: 300; }

  .print-side { left: 668px; top: 266px; font-size: 35px; line-height: 43px; text-align: left; color: var(--dark); font-weight: 400; }

  .brand { color: var(--green); font-weight: 900; font-size: 36px; letter-spacing: -0.3px; width: 257px; left: 119px; }
  .brand-top { top: 214px; }
  .brand-front { top: 447px; }
  .pet-photo { position: absolute; left: 192px; top: 266px; width: 102px; height: 124px;
    background: linear-gradient(160deg, var(--photo-light) 0%, var(--photo-mid) 55%, var(--photo-dark) 100%); }

  .band-title { left: 119px; width: 257px; top: 541px; color: var(--white); font-size: 24px; line-height: 31px; font-weight: 400; }
  .tagline { left: 119px; width: 257px; top: 626px; font-size: 19px; line-height: 24px; font-weight: 400; }
  .pets { left: 119px; width: 257px; top: 699px; font-size: 19px; font-weight: 400; }
  .net { left: 119px; width: 257px; top: 821px; color: var(--white); font-size: 14.5px; }

  .directions { left: 388px; width: 182px; top: 418px; font-size: 14px; line-height: 17.2px; font-weight: 300; color: var(--dark); }
  .directions small { font-size: 11px; }
  .green-rule { position: absolute; left: 407px; top: 525px; width: 145px; height: 1.5px; background: var(--rule); }
  .unlock { left: 386px; width: 186px; top: 530px; font-family: "Roboto Condensed", sans-serif; font-size: 16.5px; line-height: 20.5px; font-weight: 400; color: var(--dark); }
  .story { left: 389px; width: 181px; top: 586px; font-size: 13.8px; line-height: 17.2px; }
  .story p { margin-bottom: 17.2px; }

  .facts { position: absolute; left: 595px; top: 420px; width: 232px; height: 122px; border: 1.5px solid #333; font-family: "Roboto Condensed", sans-serif; font-weight: 400; color: var(--dark); }
  .facts-title { font-family: "Source Sans 3", sans-serif; font-weight: 900; font-size: 22px; text-align: center; height: 30px; line-height: 30px; border-bottom: 1.5px solid #333; }
  .facts-row { position: relative; font-size: 8.4px; line-height: 9.4px; }
  .facts-serving { height: 30px; padding: 5px 0 0 14px; border-bottom: 1.5px solid #333; }
  .facts-serving .hdr { position: absolute; right: 9px; top: 15px; }
  .facts-item { height: 36px; padding: 12px 0 0 14px; border-bottom: 1.5px solid #333; }
  .facts-item .amt { position: absolute; right: 16px; top: 12px; }
  .facts-note { padding: 6px 0 0 14px; }
  .disclaimer { left: 595px; top: 546px; width: 240px; text-align: left; font-family: "Roboto Condensed", sans-serif; font-weight: 300; font-size: 6.2px; line-height: 8.8px; }
  .store { left: 595px; top: 572px; text-align: left; font-family: "Roboto Condensed", sans-serif; font-weight: 300; font-size: 6.2px; }
  .distributor { left: 598px; top: 596px; text-align: left; font-size: 12.6px; line-height: 15.5px; font-weight: 400; }
  .distributor strong { font-weight: 600; }
  .warnings { left: 596px; top: 677px; width: 228px; text-align: left; font-size: 8px; line-height: 10.3px; font-weight: 400; }

  .care { left: 582px; width: 257px; top: 823px; color: var(--white); font-size: 14px; line-height: 17px; font-weight: 400; }

  .pitch { left: 851px; width: 178px; top: 418px; font-size: 14px; line-height: 17.2px; }
  .pitch p { margin-bottom: 17.2px; }

  .lot { left: 582px; width: 257px; top: 1031px; font-size: 16.5px; color: var(--dark); transform: rotate(180deg); font-weight: 400; }
</style>
</head>
<body>
<main class="canvas">
  <svg class="dieline" width="1097" height="1200" viewBox="0 0 1097 1200" aria-hidden="true">
    <path d="M122 196 Q124 140 161 117 L335 117 Q371 140 374 196 Z" fill="var(--white)" stroke="var(--cut)" stroke-width="1.2"/>
    <rect x="119" y="196" width="257" height="206" fill="var(--white)" stroke="var(--cut)" stroke-width="1.2"/>
    <line x1="145" y1="197" x2="350" y2="197" stroke="var(--fold)" stroke-width="1.2"/>
    <polygon points="55,408 119,403 119,865 55,859" fill="var(--white)" stroke="var(--cut)" stroke-width="1.2"/>
    <polygon points="376,260 557,260 567,374 579,386 579,402 376,402" fill="var(--green)" stroke="var(--cut)" stroke-width="1.2"/>
    <polygon points="863,260 1042,260 1042,402 841,402 841,386 855,374" fill="var(--green)" stroke="var(--cut)" stroke-width="1.2"/>
    <line x1="579" y1="402" x2="841" y2="402" stroke="var(--cut)" stroke-width="1.2"/>
    <rect x="119" y="402" width="923" height="463" fill="var(--white)"/>
    <rect x="119" y="539" width="257" height="68" fill="var(--green)"/>
    <rect x="119" y="817" width="923" height="48" fill="var(--green)"/>
    <path d="M119 402 V865 M1042 402 V865" stroke="var(--cut)" stroke-width="1.2" fill="none"/>
    <path d="M119 865 H376" stroke="var(--cut)" stroke-width="1.2"/>
    <path d="M119 402 H376 M376 402 V865 M582 402 V865 M839 402 V865 M376 865 H1042" stroke="var(--fold)" stroke-width="1.2" fill="none"/>
    <polygon points="379,865 582,865 582,1008 402,1008 392,893 379,881" fill="var(--green)" stroke="var(--cut)" stroke-width="1.2"/>
    <polygon points="839,865 1042,865 1042,881 1030,893 1020,1008 839,1008" fill="var(--green)" stroke="var(--cut)" stroke-width="1.2"/>
    <path d="M585 1072 Q588 1125 622 1149 L798 1149 Q832 1125 836 1072 Z" fill="var(--green)" stroke="var(--cut)" stroke-width="1.2"/>
    <rect x="582" y="865" width="257" height="207" fill="var(--green)" stroke="var(--cut)" stroke-width="1.2"/>
    <line x1="610" y1="1071" x2="812" y2="1071" stroke="var(--fold)" stroke-width="1.2"/>
    <line x1="582" y1="866" x2="839" y2="866" stroke="var(--fold)" stroke-width="1.2"/>
  </svg>

  <div class="txt print-side">PRINT<br>SIDE</div>

  <div class="txt brand brand-top">Marivita</div>
  <div class="pet-photo" role="img" aria-label="Photo of a golden retriever sitting beside a kitten"></div>

  <div class="txt brand brand-front">Marivita</div>
  <div class="txt band-title">100% Pure Marine<br>Phytoplankton Powder</div>
  <div class="txt tagline">Foundational Nutrition<br>&amp; Super-Antioxidant</div>
  <div class="txt pets">For Dogs &amp; Cats</div>
  <div class="txt net">15g</div>

  <div class="txt directions">Directions: For dogs &amp; cats <small>1/16</small>tsp once per day. Administer orally. To be mixed into food. <small>1/16</small>tsp = <small>1/2</small> the included scoop.</div>
  <div class="green-rule"></div>
  <div class="txt unlock">Unlock Nature’s<br>Nutrient Treasure:</div>
  <div class="txt story cond">
    <p>Phytoplankton is the foundation of life, It is the first plant in the entire food chain.</p>
    <p>Phytoplankton is a microscopic powerhouse. Your pet’s body absorbs billions of phytoplankton with every serving.</p>
    <p>Packed with the building blocks of life, phytoplankton addresses multiple aspects of your pet’s health in one simple supplement.</p>
  </div>

  <section class="facts">
    <div class="facts-title">Supplement Facts</div>
    <div class="facts-row facts-serving">Serving Size: 1 Scoop/Day<br>Servings per Container: 30<span class="hdr">Amount per Serving &nbsp;&nbsp;%DV</span></div>
    <div class="facts-row facts-item">Microalgae Nannochloropsis Gaditana<span class="amt">500mg &nbsp;&nbsp;&nbsp;‡</span></div>
    <div class="facts-row facts-note">‡ Daily value not established.</div>
  </section>
  <div class="txt disclaimer">These statements have not been evaluated by the Food and Drug Administrations.<br>This products is not intended to diagnose, treat, cure, or prevent any disease.</div>
  <div class="txt store">Store in a cool, dry place.</div>
  <div class="txt distributor"><strong>Distributed By::</strong><br>Tidewell Nutrition Inc.<br>42-8 Harbour Road,<br>Seabrook, Nova Scotia Canada<br>B3K 2P9</div>
  <div class="txt warnings">Warnings: Check with a qualified healthcare professional before using this product if you are pregnant, breastfeeding, or taking blood thinners. You should call your doctor for medical advice about serious adverse events. To report a serious adverse event or obtain product information contact: &nbsp;1 800 555 0182</div>
  <div class="txt care">Customer Care: 1 800 555 0182<br>tidewellnutrition.com</div>

  <div class="txt pitch cond">
    <p>Our premium phytoplankton powder is a extraordinary supplement. &nbsp;It infuses your pet’s body with pure, plant-based nutrients and potent antioxidants.</p>
    <p>Phytoplankton goes beyond ordinary supplements; it's a path to optimal health. In just a few weeks, your pet will experience a feeling of calm and strength, the kind of wellness our customers often say they've been seeking.</p>
    <p>Join those who have discovered the transformative power of phytoplankton. See the difference for yourself and understand why it's not just a supplement, but a revolution in pet health and vitality.</p>
  </div>

  <div class="txt lot">Exp: 22025/03/Lot No.:1 2222</div>
</main>
</body>
</html>
```